We need your help in designing the graphical look of the home page of our web site: Quellnest.com.

Quellnest is an FREE online service that brings consumers and service providers together through online reservations.

Our service is in fact a web application (similar to brindlo calendar), so we will be using forms, widgets, menus and standard web controls (buttons, fields, links, etc). We need a design that will be easy to integrate with our programming.

This design project is for the HOME page, but we will choose the designer that will design the web page in photoshop in layers, so we can easily derive our other secondary pages ourselves.

If you have any questions please send us a message and we will gladly update the brief with a response.

Happy Designing!
Updates

Hi all, the menu on the home page should be something standard, like: Pricing, features, how it works.

once a user is logged in, they will see their toolbox at all times:
- My Nest (links to their main page of bookings)
- My Faborites (view favorite businesses and book quickly with them)
- Settings (set parameters of their account)

There should be a My Profile page as well. 

Thanks!

Reason: I have extended the deadline to receive more designs.

Hi All,

UPDATE: we changed our vision of the home page to have a much simpler design.  something along the lines of tumbrella vexnor and mor tan.

HOME PAGE:
light colors with white background.  simple, simple, simple!

header should not be big, logo, change language link. try with search bar (what and where).

body should be simple, with an image + register form only.

footer with links to pages for more info:
- Privacy,
- Getting started
- How it works
- Contact us
- FAQ
- Pricing

LOGGED IN PAGE:
when logged in, the header can be the same or reduced to maximize the "working area" (body).
body can be a 2 or 3 column design, as we have a main working area.  in your design, show a calendar.  we need a toolbar (side or top) that will have these buttons, links: MyNest, My Favorites, Settings, My Profile.
We need a section that will display latest messages or notifications.
keep the footer with the links.

Thank you all.

Reason: Holidays

Reason: holidays... lets spend time with our families!

Target Market(s)

Young and mobile consumers + professionals, businesses, restaurants and commerces wishing to offer online reservations (appointments and reservations)

Industry/Entity Type

Brindlo

Requirements
Must have
• - Easy to integrate with web programming
- light weight visual design. We want something with light tone colors as background
- home page will have a content slider that will show some catch phrases.
- Overall design should be more on the "cartoony" side. Should give a casual, humour and friendly ambiance.

The home page should have these sections:
- a search section for consumers to find local businesses. They will search by specifying "What?" & "Where?"
- a content slider that will cycle through catch phrases and features. Each pane should have an image representative of the text.
- have 4 highlighted sections
- QuellNest is great for (list of different businesses types that use quelnest)
- QuellNest is available for FREE to everyone
- Main features list (accept 24/7 reservations, never reveal your schedule, automatic reminders, marketing campaigns)
- The more you quell, the more you save! (info on our loyalty program that entitles consumers to greater savings and benefits).

One a user logs in, all the certer page info will be replaced by a content div that will allow content to display based on selected menu item
- My Nest (opens the main section where all happens. This section should have a design that gives the impression that we're looking in a box)
- My Profile
- My Favorites
Should not have
• - Don't use actual photos of real people, rather opt for sketches and cartoony characters.

```html
<!DOCTYPE html>
<html lang="en">
<head>
<meta charset="utf-8">
<title>QuellNest – Schedule can be easy</title>
<link rel="stylesheet" href="https://fonts.googleapis.com/css2?family=Arimo:wght@400;700&family=Cinzel:wght@700&family=Rubik+Dirt&family=Nunito:wght@800&display=swap">
<style>
  :root {
    --ink: #111111;
    --black: #000000;
    --cyan: #1ba6c7;
    --cyan-light: #36e2f6;
    --cyan-deep: #1696b6;
    --page: #eeeeee;
    --panel: #ffffff;
    --line: #d6d6d6;
    --muted: #4a4a4a;
    --field: #e2e2e2;
    --icon: #2b2b2b;
    --btn-top: #4fb8ea;
    --btn-bottom: #1f86c4;
  }
  * { box-sizing: border-box; margin: 0; padding: 0; }
  html, body { width: 960px; height: 1200px; overflow: hidden; }
  body {
    position: relative;
    background: var(--page);
    font-family: "Arimo", Arial, sans-serif;
    color: var(--ink);
  }
  .abs { position: absolute; }

  /* Header */
  .site-header { left: 0; top: 0; width: 960px; height: 98px; background: var(--black); }
  .brand { left: 96px; top: 30px; display: flex; align-items: center; gap: 10px; }
  .brand-square { width: 30px; height: 30px; background: var(--cyan); }
  .brand-name { font-size: 24px; font-weight: 700; color: var(--cyan); letter-spacing: 1px; }
  .account-links { left: 722px; top: 0; height: 33px; display: flex; align-items: center; font-size: 12px; }
  .account-links .login { color: var(--cyan); }
  .account-links .or { color: #fff; margin: 0 8px 0 6px; }
  .account-links .register {
    width: 74px; height: 33px; line-height: 33px; text-align: center;
    background: linear-gradient(#f4f4f4, #d8d8d8); color: var(--ink);
    border-radius: 0 0 3px 3px;
  }
  .main-nav { left: 424px; top: 58px; display: flex; gap: 37px; font-size: 12.5px; color: #fff; }

  /* Hero */
  .hero-band { left: 0; top: 98px; width: 960px; height: 310px;
    background: linear-gradient(var(--cyan), var(--cyan-light)); }
  .hero-panel { left: 96px; top: 128px; width: 768px; height: 280px;
    background: linear-gradient(#ffffff, #e8e8e8); }
  .hero-art { left: 70px; top: 20px; width: 250px; height: 260px;
    background: linear-gradient(160deg, #3a3f48, #15171b 55%, #9aa3ab); border-radius: 26px 26px 0 0; }
  .hero-title { left: 407px; top: 98px; }
  .hero-title .big { font-family: "Rubik Dirt", Impact, sans-serif; font-size: 58px; line-height: 58px; color: var(--black); }
  .hero-title .soft { font-family: "Nunito", Arial, sans-serif; font-size: 56px; color: var(--cyan); }
  .slider-arrow { width: 30px; height: 46px; top: 246px; background: var(--cyan-deep); display: flex; align-items: center; justify-content: center; }
  .slider-arrow.prev { left: 96px; border-radius: 0 23px 23px 0; }
  .slider-arrow.next { left: 834px; border-radius: 23px 0 0 23px; }

  .feature-strip { left: 96px; top: 408px; width: 768px; height: 94px; display: flex;
    background: linear-gradient(#fafafa, #eeeeee); box-shadow: 0 2px 3px rgba(0,0,0,.15); }
  .feature-item { flex: 1; display: flex; gap: 17px; padding: 22px 0 0 22px; border-right: 1px solid var(--line); }
  .feature-item:last-child { border-right: 0; }
  .feature-item h3 { font-size: 12px; font-weight: 700; margin-bottom: 4px; }
  .feature-item p { font-size: 9.5px; line-height: 12px; color: var(--muted); width: 170px; }

  /* Search */
  .box { background: var(--panel); border: 1px solid var(--line); border-radius: 6px; box-shadow: 0 1px 2px rgba(0,0,0,.08); }
  .section-title { font-family: "Cinzel", Georgia, serif; font-size: 16px; font-weight: 700; color: var(--ink); }
  .section-title span { color: var(--cyan); }
  .search-box { left: 96px; top: 538px; width: 768px; height: 84px; }
  .search-box .section-title { position: absolute; left: 22px; top: 10px; }
  .search-field { top: 36px; height: 34px; background: var(--field); border: 1px solid #cfcfcf; border-radius: 3px;
    font-size: 13px; color: #8a8a8a; padding: 9px 0 0 9px; }
  .search-field.what { left: 20px; width: 330px; }
  .search-field.where { left: 366px; width: 328px; }
  .search-button { left: 709px; top: 36px; width: 39px; height: 34px; border-radius: 3px;
    background: linear-gradient(var(--btn-top), var(--btn-bottom)); display: flex; align-items: center; justify-content: center; }

  /* Main feature cards */
  .card { width: 371px; height: 130px; background: linear-gradient(#ffffff, #eeeeee); }
  .card-art { left: 22px; top: 24px; width: 72px; height: 82px; border-radius: 36px;
    background: radial-gradient(circle at 40% 35%, #5a5a5a, #1c1c1c); }
  .card h2 { position: absolute; left: 118px; top: 30px; font-size: 15px; font-weight: 700; }
  .card p { position: absolute; left: 118px; top: 57px; font-size: 9.5px; color: var(--muted); }
  .learn-more { right: 0; bottom: 0; width: 113px; height: 30px; border-radius: 3px 0 5px 0;
    background: linear-gradient(var(--btn-top), var(--btn-bottom)); color: #fff; font-size: 12px; font-weight: 700;
    display: flex; align-items: center; justify-content: center; gap: 6px; }
  .learn-more i { width: 16px; height: 16px; border-radius: 50%; background: #e9f4fb; display: inline-block; position: relative; }
  .learn-more i::after { content: "»"; position: absolute; left: 4px; top: -1px; font-style: normal; font-size: 12px; color: var(--btn-bottom); }

  /* Great for */
  .great-for { left: 96px; top: 973px; width: 768px; height: 158px; }
  .great-for .section-title { position: absolute; left: 22px; top: 10px; }
  .client-slot { top: 37px; width: 143px; height: 102px; background: linear-gradient(#f2f2f2, #e4e4e4);
    border: 1px solid #dadada; display: flex; align-items: center; gap: 6px; padding-left: 14px; }
  .client-slot span { font-family: "Cinzel", Georgia, serif; font-size: 16px; color: #3a3a3a; line-height: 21px; }
  .carousel-btn { top: 73px; width: 27px; height: 27px; border-radius: 2px;
    background: linear-gradient(var(--btn-top), var(--btn-bottom)); display: flex; align-items: center; justify-content: center; }

  /* Footer */
  .site-footer { left: 0; top: 1162px; width: 960px; height: 38px; background: var(--ink);
    color: #fff; font-size: 10px; padding: 14px 0 0 105px; }
  .site-footer span { color: var(--cyan); }
</style>
</head>
<body>

<header class="site-header abs">
  <div class="brand abs"><div class="brand-square"></div><div class="brand-name">QuellNest</div></div>
  <div class="account-links abs"><span class="login">LOGIN</span><span class="or">OR</span><span class="register">REGISTER</span></div>
  <nav class="main-nav abs"><span>HOME</span><span>FEATURES</span><span>PRICING</span><span>PURCHASE</span><span>SUPPORT</span></nav>
</header>

<div class="hero-band abs"></div>
<section class="hero-panel abs">
  <div class="hero-art abs" role="img" aria-label="Smartphone showing a December calendar with a magnifying glass over it"></div>
  <div class="hero-title abs">
    <div class="big">SCHEDULE</div>
    <div><span class="soft">can be</span> <span class="big">easy</span></div>
  </div>
</section>
<div class="slider-arrow prev abs"><svg width="12" height="14" viewBox="0 0 12 14"><path d="M10 1 3 7l7 6" fill="none" stroke="#000" stroke-width="3"/></svg></div>
<div class="slider-arrow next abs"><svg width="12" height="14" viewBox="0 0 12 14"><path d="M2 1l7 6-7 6" fill="none" stroke="#000" stroke-width="3"/></svg></div>

<section class="feature-strip abs">
  <div class="feature-item">
    <svg width="38" height="38" viewBox="0 0 38 38"><rect x="2" y="6" width="34" height="30" rx="2" fill="#111"/><rect x="6" y="16" width="26" height="16" fill="#fff"/><g fill="#111" stroke="#fff" stroke-width="1"><rect x="8" y="1" width="4" height="10"/><rect x="14" y="1" width="4" height="10"/><rect x="20" y="1" width="4" height="10"/><rect x="26" y="1" width="4" height="10"/></g></svg>
    <div><h3>Get your schedule</h3><p>You can create your schedule by just simply set your date and time.</p></div>
  </div>
  <div class="feature-item">
    <svg width="38" height="38" viewBox="0 0 38 38"><rect x="2" y="3" width="34" height="32" rx="2" fill="#111"/><rect x="6" y="11" width="26" height="20" fill="#fff"/><circle cx="7" cy="7" r="1.5" fill="#fff"/><circle cx="12" cy="7" r="1.5" fill="#fff"/><path d="M17 15l9 6-4 1 3 5-2 1-3-5-3 3z" fill="#111"/></svg>
    <div><h3>Online Reservation</h3><p>You can make online reservation from anywhere and aytime you want.</p></div>
  </div>
  <div class="feature-item">
    <svg width="38" height="38" viewBox="0 0 38 38"><path d="M3 13h7l10-9v30l-10-9H3z" fill="#111"/><path d="M25 13q4 6 0 12M29 9q8 10 0 20" fill="none" stroke="#111" stroke-width="3"/></svg>
    <div><h3>Effective Reminder</h3><p>You will not mess up your schedule because you wil get alarmed.</p></div>
  </div>
</section>

<section class="search-box box abs">
  <h2 class="section-title">SEARCH <span>LOCAL BUSINESS</span></h2>
  <div class="search-field what abs">what</div>
  <div class="search-field where abs">where</div>
  <div class="search-button abs"><svg width="22" height="22" viewBox="0 0 22 22"><circle cx="13" cy="9" r="6" fill="none" stroke="#111" stroke-width="3"/><path d="M9 13 2 20" stroke="#111" stroke-width="4" stroke-linecap="round"/></svg></div>
</section>

<article class="card box abs" style="left:96px;top:653px">
  <div class="card-art abs" role="img" aria-label="Stopwatch icon"></div>
  <h2>Automatic reminders</h2><p>Automates give notification about your schedules.</p>
  <div class="learn-more abs">LEARN MORE <i></i></div>
</article>
<article class="card box abs" style="left:492px;top:653px">
  <div class="card-art abs" role="img" aria-label="Light bulb icon"></div>
  <h2>Never reveal your schedule</h2><p>Track success with user-friendly charts and reports.</p>
  <div class="learn-more abs">LEARN MORE <i></i></div>
</article>
<article class="card box abs" style="left:96px;top:811px">
  <div class="card-art abs" role="img" aria-label="Business person silhouette icon"></div>
  <h2>Marketing campaigns</h2><p>Send email newsletters, mailshots and much more.</p>
  <div class="learn-more abs">LEARN MORE <i></i></div>
</article>
<article class="card box abs" style="left:492px;top:811px">
  <div class="card-art abs" role="img" aria-label="Wall clock icon"></div>
  <h2>Accept 24/7 reservations</h2><p>Stay up, running 24/7 and keep your data backed up</p>
  <div class="learn-more abs">LEARN MORE <i></i></div>
</article>

<section class="great-for box abs">
  <h2 class="section-title">QUELLNEST <span>IS GREAT FOR</span></h2>
  <div class="carousel-btn abs" style="left:22px"><svg width="12" height="14" viewBox="0 0 12 14"><path d="M10 1 3 7l7 6" fill="none" stroke="#111" stroke-width="3"/></svg></div>
  <div class="client-slot abs" style="left:65px"><svg width="34" height="58" viewBox="0 0 34 58"><path d="M22 0 2 34h13L9 58l23-36H19L28 0z" fill="#3a3a3a"/></svg><span>CLIENT<br>LOGO</span></div>
  <div class="client-slot abs" style="left:230px"><svg width="34" height="58" viewBox="0 0 34 58"><path d="M22 0 2 34h13L9 58l23-36H19L28 0z" fill="#3a3a3a"/></svg><span>CLIENT<br>LOGO</span></div>
  <div class="client-slot abs" style="left:395px"><svg width="34" height="58" viewBox="0 0 34 58"><path d="M22 0 2 34h13L9 58l23-36H19L28 0z" fill="#3a3a3a"/></svg><span>CLIENT<br>LOGO</span></div>
  <div class="client-slot abs" style="left:561px"><svg width="34" height="58" viewBox="0 0 34 58"><path d="M22 0 2 34h13L9 58l23-36H19L28 0z" fill="#3a3a3a"/></svg><span>CLIENT<br>LOGO</span></div>
  <div class="carousel-btn abs" style="left:719px"><svg width="12" height="14" viewBox="0 0 12 14"><path d="M2 1l7 6-7 6" fill="none" stroke="#111" stroke-width="3"/></svg></div>
</section>

<footer class="site-footer abs">Copyright (c) 2011 <span>QuellNest</span>. All rights reserved.</footer>

</body>
</html>
```